Lantern Marketing Group (LMG)

This is for my business cards. I want a Nice anfd Elegant Business Card to be Designed, Using more or less of the same colors of my logo that i have attached.i would like to have these business cards forever

Thank you

Thank you

Thank you

Contact Information for Business Card

Calvin Ortega
Lantern Marketing Group
C.(555) 482-1306
E-Mail. COrtega@lanternmgroup.example

Font styles to use
Serif
Sans Serif

Colors
d0dfed
cbcbcb
cee9f5

Requirements
Must have
• (LMG)
• Lantern Marketing Group
Nice to have
• 3D affects
Should not have
• Please try not using the flat version of the logo try and use the 3d version please

```html
<!DOCTYPE html>
<html lang="en">
<head>
<meta charset="utf-8">
<title>Lantern Marketing Group — Business Card</title>
<link rel="stylesheet" href="https://fonts.googleapis.com/css2?family=Open+Sans:wght@400;700&display=swap">
<style>
  :root {
    --page: #eceff2;
    --card: #f7f9fb;
    --card-tint: #e8f0f6;
    --brand-blue: #1f74c6;
    --band-blue: #2f8fd3;
    --band-gray: #9a9a9a;
    --text-gray: #8a8a8a;
    --shadow: rgba(20, 40, 60, 0.18);
  }
  * { box-sizing: border-box; margin: 0; padding: 0; }
  html, body { width: 1200px; height: 900px; overflow: hidden; }
  body {
    background: var(--page);
    font-family: "Open Sans", Arial, sans-serif;
    position: relative;
  }
  .card {
    position: absolute;
    left: 250px;
    width: 700px;
    height: 400px;
    background: linear-gradient(180deg, var(--card) 0%, var(--card-tint) 100%);
    box-shadow: 0 6px 18px var(--shadow);
    overflow: hidden;
  }
  .card--front { top: 40px; }
  .card--back { top: 460px; }
  .card__bands { position: absolute; inset: 0; width: 700px; height: 400px; }
  .brand {
    position: absolute;
    display: flex;
    flex-direction: column;
    align-items: center;
    color: var(--brand-blue);
    font-weight: 700;
    text-transform: uppercase;
    letter-spacing: 0.08em;
    line-height: 1.15;
  }
  .brand__square {
    width: 72px; height: 72px;
    background: var(--brand-blue);
    margin-bottom: 14px;
  }
  .brand__name { font-size: 24px; text-align: center; }
  .card--front .brand { left: 0; right: 0; top: 62px; }
  .card--back .brand { left: 70px; top: 150px; width: 260px; }
  .card--back .brand__name { font-size: 21px; }
  .contact {
    position: absolute;
    right: 44px;
    top: 150px;
    text-align: right;
  }
  .contact__name { color: var(--brand-blue); font-size: 26px; font-weight: 700; line-height: 1.1; }
  .contact__role { color: var(--text-gray); font-size: 15px; margin-bottom: 22px; }
  .contact__line {
    display: flex; justify-content: flex-end; align-items: center; gap: 8px;
    color: var(--brand-blue); font-size: 16px; line-height: 1.7;
  }
  .contact__icon { width: 15px; height: 15px; fill: none; stroke: var(--text-gray); stroke-width: 1.6; }
</style>
</head>
<body>
  <section class="card card--front" aria-label="Card front">
    <svg class="card__bands" viewBox="0 0 700 400" aria-hidden="true">
      <polygon points="0,300 460,300 440,316 0,316" fill="var(--band-gray)"/>
      <polygon points="500,270 700,270 700,354 0,354 0,328 450,328" fill="var(--band-blue)"/>
    </svg>
    <div class="brand">
      <div class="brand__square"></div>
      <div class="brand__name">Lantern Marketing Group</div>
    </div>
  </section>

  <section class="card card--back" aria-label="Card back">
    <svg class="card__bands" viewBox="0 0 700 400" aria-hidden="true">
      <polygon points="0,14 700,14 700,62 400,62 370,40 0,40" fill="var(--band-blue)"/>
      <polygon points="0,48 352,48 372,64 0,64" fill="var(--band-gray)"/>
      <polygon points="0,318 440,318 460,302 0,302" fill="none"/>
      <polygon points="0,314 440,314 418,330 0,330" fill="var(--band-gray)"/>
      <polygon points="480,290 700,290 700,384 0,384 0,344 430,344" fill="var(--band-blue)"/>
    </svg>
    <div class="brand">
      <div class="brand__square"></div>
      <div class="brand__name">Lantern Marketing Group</div>
    </div>
    <div class="contact">
      <div class="contact__name">Calvin Ortega</div>
      <div class="contact__role">Owner</div>
      <div class="contact__line">
        <span>(555) 482-1306</span>
        <svg class="contact__icon" viewBox="0 0 16 16" aria-hidden="true"><path d="M3 1.5l3 3-1.6 1.8a9 9 0 0 0 5.3 5.3L11.5 10l3 3-1.8 1.8C7.5 14.5 1.5 8.5 1.2 3.3z"/></svg>
      </div>
      <div class="contact__line">
        <span>COrtega@lanternmgroup.example</span>
        <svg class="contact__icon" viewBox="0 0 16 16" aria-hidden="true"><rect x="1.5" y="3.5" width="13" height="9"/><path d="M1.5 3.5l6.5 5 6.5-5"/></svg>
      </div>
    </div>
  </section>
</body>
</html>
```